Venbrisk Card

We want a business card that shows people who we are the log attached was designed by the designers on graft hive,we are using the OO in the logo (speech bubbles as our icon,so please make that part of the card ) keep the colouring the same as the logo design and we will be using high end production on the card using silver foil as the icon to make it stand out.
As Venbrisk we specialise in finding influencers through social networks for brands, so if you used yammo to comment about sports products and you were followed by of lot of users and interacted with those users then the algorithm finds you and we contact you to work for our clients as a company we then have a set of influencers that we use to support new sports products.
Also we use our algorithm to help athletes,models etc to be scored via there digital influence so when say Orvel QD ask me to find a skater that is not so much a podium rider but is more digital focused for a digital campaign then we work out who those guys or girls are to help Orvel QD
Venbrisk is the name of the product and company, However I just wanted to give you the rationale of why we chose venbrisk in the first place. Aldo itself is an 'abbreviation' from the proper name Aldemar Fusk from Keeper of the Vales. The character was able to look into the morvendal (sometimes translated as "Seeing Stone" but literally meaning "Farsighted" or "One that Sees from Afar") and see into the far corners of the Universe. Much in the same way as the platform has been developed is able to look into the far corners of the social network arena to help brands and Athletes will be able to see how they rated....but don't worry i don't go running around in the woods with a foam Axe and an army of dwarfs!!!
Digital Directors,Brand Directors,Athletes,Models,Celebrities and agents
Business

```html
<!DOCTYPE html>
<html lang="en">
<head>
<meta charset="utf-8">
<title>Venbrisk Business Cards</title>
<link href="https://fonts.googleapis.com/css2?family=Fira+Sans:wght@300;400;600&display=swap" rel="stylesheet">
<style>
:root{
  --brand-blue:#4fbdee;
  --brand-grey:#808285;
  --paper:#ffffff;
  --edge:#e6e6e6;
}
*{margin:0;padding:0;box-sizing:border-box}
html,body{width:1200px;height:1000px;overflow:hidden;background:var(--paper);font-family:"Fira Sans",sans-serif}
.sheet{position:relative;width:1200px;height:1000px}
.card{position:absolute;width:547px;height:354px;overflow:hidden}
.card--white{background:var(--paper);border:1px solid var(--edge)}
.card--front.card--blue{background:var(--brand-blue)}

/* front */
.wordmark{position:absolute;left:0;right:0;top:126px;text-align:center;font-weight:600;font-size:96px;line-height:1;letter-spacing:-2px}
.card--blue .wordmark{color:var(--paper)}
.card--white .wordmark{color:var(--brand-blue)}
.web-line{position:absolute;left:94px;width:359px;top:259px;display:flex;align-items:center;gap:12px}
.web-line .dots{flex:1;border-top:2px dotted currentColor;height:0}
.web-line .url{font-weight:600;font-size:19px;white-space:nowrap}
.card--blue .web-line{color:var(--paper)}
.card--white .web-line{color:var(--brand-blue)}

/* back */
.back-face{position:absolute;left:0;top:0;width:547px;height:310px}
.card--blue .back-face{background:var(--brand-blue)}
.name-disc{position:absolute;left:58px;top:44px;width:194px;height:194px;border-radius:50%;display:flex;flex-direction:column;align-items:center;justify-content:center;text-align:center;font-size:20px;line-height:27px}
.name-disc .person{font-weight:600}
.name-disc .role{font-weight:300}
.card--blue .name-disc{background:var(--paper);color:var(--brand-blue)}
.card--white .name-disc{background:var(--brand-blue);color:var(--paper)}
.contacts{position:absolute;left:298px;top:64px;font-size:16px;line-height:22px}
.contacts dt{font-weight:600}
.contacts dd{font-weight:300;margin-bottom:13px}
.card--blue .contacts{color:var(--paper)}
.card--white .contacts{color:var(--brand-blue)}

.social-band{position:absolute;left:0;top:310px;width:547px;height:44px;font-size:16px}
.card--blue .social-band{background:var(--paper);color:var(--brand-blue);border-bottom:1px solid var(--edge)}
.card--white .social-band{background:var(--brand-blue);color:var(--paper)}
.social-label{position:absolute;left:57px;top:0;line-height:44px;font-weight:600}
.social-item{position:absolute;top:0;height:44px;display:flex;align-items:center;gap:8px;font-weight:300}
.social-item .chip{width:15px;height:15px;border-radius:2px;background:currentColor}
.social-item--first{left:188px}
.social-item--second{left:292px}
.social-item--third{left:396px}
</style>
</head>
<body>
<main class="sheet">

  <section class="card card--front card--blue" style="left:41px;top:109px">
    <div class="wordmark">venbrisk</div>
    <div class="web-line"><span class="dots"></span><span class="url">www.venbrisk.co.uk</span><span class="dots"></span></div>
  </section>

  <section class="card card--back card--blue" style="left:611px;top:109px">
    <div class="back-face">
      <div class="name-disc"><span class="person">Ned Marlow</span><span class="role">Director</span></div>
      <dl class="contacts">
        <dt>Telephone</dt><dd>020 7946 0321</dd>
        <dt>Mobile</dt><dd>07700 900482</dd>
        <dt>eMail</dt><dd>nedmarlow@venbrisk.co.uk</dd>
      </dl>
    </div>
    <div class="social-band">
      <span class="social-label">Social</span>
      <span class="social-item social-item--first"><span class="chip"></span>venbrisk</span>
      <span class="social-item social-item--second"><span class="chip"></span>venbrisk</span>
      <span class="social-item social-item--third"><span class="chip"></span>venbrisk</span>
    </div>
  </section>

  <section class="card card--front card--white" style="left:41px;top:487px">
    <div class="wordmark">venbrisk</div>
    <div class="web-line"><span class="dots"></span><span class="url">www.venbrisk.co.uk</span><span class="dots"></span></div>
  </section>

  <section class="card card--back card--white" style="left:611px;top:487px">
    <div class="back-face">
      <div class="name-disc"><span class="person">Ned Marlow</span><span class="role">Director</span></div>
      <dl class="contacts">
        <dt>Telephone</dt><dd>020 7946 0321</dd>
        <dt>Mobile</dt><dd>07700 900482</dd>
        <dt>eMail</dt><dd>nedmarlow@venbrisk.co.uk</dd>
      </dl>
    </div>
    <div class="social-band">
      <span class="social-label">Social</span>
      <span class="social-item social-item--first"><span class="chip"></span>venbrisk</span>
      <span class="social-item social-item--second"><span class="chip"></span>venbrisk</span>
      <span class="social-item social-item--third"><span class="chip"></span>venbrisk</span>
    </div>
  </section>

</main>
</body>
</html>
```